Business cards for 3 Realtors at one brokerage

We will need a business card template that can be projected on 3 business cards. Harborline Homes & Capital Corp. has 3 realtors on staff Dale, Owen, and Marcus. We all want a business card that shows our new logo and information. I will attach many versions of our Logo as well as head shots for each realtor (Owen- Long hair, youngest. Marcus- Suit jacket, parted hair cut. Dale- Angled Pose, Shirt and Tie.) I have attached our information below.

Dale Pinsworth
801-555-0147
dale@harborlinehomesco.com
Principal Broker

Marcus Ferndale
801-555-0192
marcus@harborlinehomesco.com
Real Estate Agent

Owen Ferndale
801-555-0163
owen@harborlinehomesco.com
Real Estate Agent

Harborline Homes & Capital Corp.
HarborlineHomesCo.com
2918 E 8250 Suite 207-316, Willow Bend, UT 84071

Please feel free to reach out with any questions, comments, or concerns.

```html
<!DOCTYPE html>
<html lang="en">
<head>
<meta charset="utf-8">
<title>Harborline Homes &amp; Capital Corp. – Business Cards</title>
<link href="https://fonts.googleapis.com/css2?family=Poppins:wght@400;500;600;700&display=swap" rel="stylesheet">
<style>
  :root {
    --page-bg: #e4e4e4;
    --brand-blue: #4fa3db;
    --brand-blue-dark: #3d8fc8;
    --ink: #5a5a5a;
    --ink-soft: #6b6b6b;
    --card-white: #ffffff;
    --photo-light: #b9b9b9;
    --photo-dark: #6e6e6e;
  }
  * { box-sizing: border-box; margin: 0; padding: 0; }
  html, body {
    width: 1200px; height: 852px; overflow: hidden;
    background: var(--page-bg);
    font-family: "Poppins", sans-serif;
  }
  .card {
    position: absolute;
    width: 560px; height: 320px;
    border-radius: 18px;
    overflow: hidden;
    box-shadow: 0 10px 24px rgba(0,0,0,0.18);
  }

  /* Back of card */
  .card-back {
    left: 70px; top: 70px;
    background: var(--brand-blue);
    color: var(--card-white);
    display: flex; flex-direction: column; align-items: center; justify-content: center;
    text-align: center;
  }
  .card-back .brand-mark {
    width: 64px; height: 64px; border-radius: 50%;
    border: 4px solid var(--card-white);
    margin-bottom: 14px;
  }
  .card-back .brand-name {
    font-weight: 600; font-size: 30px; letter-spacing: 1px; line-height: 1.05;
  }
  .card-back .brand-sub {
    font-weight: 600; font-size: 11px; letter-spacing: 4px; margin-top: 4px;
  }
  .card-back .website {
    font-weight: 500; font-size: 13px; letter-spacing: 0.5px; margin-top: 34px;
  }

  /* Front of card */
  .card-front {
    left: 570px; top: 460px;
    background: var(--card-white);
  }
  .card-front .headshot {
    position: absolute; inset: 0;
  }
  .front-content {
    position: absolute; left: 34px; top: 28px;
    color: var(--ink);
  }
  .front-brand .brand-mark {
    width: 46px; height: 46px; border-radius: 50%;
    border: 3px solid var(--brand-blue);
    margin-left: 30px; margin-bottom: 8px;
  }
  .front-brand .brand-name {
    font-weight: 600; font-size: 20px; letter-spacing: 0.5px; line-height: 1.05;
  }
  .front-brand .brand-sub {
    font-weight: 600; font-size: 8px; letter-spacing: 3px; margin-top: 2px;
  }
  .agent-name {
    font-weight: 700; font-size: 16px; letter-spacing: 0.5px; margin-top: 20px;
  }
  .agent-title {
    font-weight: 500; font-size: 11px; color: var(--brand-blue); letter-spacing: 0.5px;
  }
  .contact-list { list-style: none; margin-top: 8px; }
  .contact-list li {
    display: flex; align-items: flex-start; gap: 8px;
    font-size: 11.5px; color: var(--ink-soft); line-height: 1.45;
  }
  .contact-list svg { width: 11px; height: 11px; margin-top: 3px; flex: none; fill: var(--brand-blue); }
</style>
</head>
<body>

  <section class="card card-back">
    <div class="brand-mark"></div>
    <div class="brand-name">HARBORLINE HOMES</div>
    <div class="brand-sub">&amp; CAPITAL CORP.</div>
    <div class="website">HARBORLINEHOMESCO.COM</div>
  </section>

  <section class="card card-front">
    <svg class="headshot" viewBox="0 0 560 320" width="560" height="320">
      <defs>
        <radialGradient id="photoTone" cx="0.6" cy="0.4" r="0.7">
          <stop offset="0" stop-color="var(--photo-light)"/>
          <stop offset="1" stop-color="var(--photo-dark)"/>
        </radialGradient>
      </defs>
      <circle cx="520" cy="80" r="262" fill="none" stroke="var(--brand-blue)" stroke-width="5"/>
      <circle cx="520" cy="80" r="252" fill="url(#photoTone)" role="img" aria-label="Headshot of Dale Pinsworth in a striped shirt and tie"/>
    </svg>

    <div class="front-content">
      <div class="front-brand">
        <div class="brand-mark"></div>
        <div class="brand-name">HARBORLINE HOMES</div>
        <div class="brand-sub">&amp; CAPITAL CORP.</div>
      </div>
      <div class="agent-name">DALE PINSWORTH</div>
      <div class="agent-title">PRINCIPAL BROKER</div>
      <ul class="contact-list">
        <li>
          <svg viewBox="0 0 24 24"><path d="M6.6 10.8a15.1 15.1 0 0 0 6.6 6.6l2.2-2.2a1 1 0 0 1 1-.25 11.4 11.4 0 0 0 3.6.57 1 1 0 0 1 1 1V20a1 1 0 0 1-1 1A17 17 0 0 1 3 4a1 1 0 0 1 1-1h3.5a1 1 0 0 1 1 1c0 1.25.2 2.45.57 3.57a1 1 0 0 1-.25 1z"/></svg>
          801-555-0147
        </li>
        <li>
          <svg viewBox="0 0 24 24"><path d="M2 5h20v14H2z M3.5 6.5 12 13l8.5-6.5" stroke="#fff" stroke-width="1.6"/></svg>
          dale@harborlinehomesco.com
        </li>
        <li>
          <svg viewBox="0 0 24 24"><circle cx="12" cy="12" r="10"/><path d="M2 12h20M12 2c3 3 3 17 0 20M12 2c-3 3-3 17 0 20" stroke="#fff" stroke-width="1.4" fill="none"/></svg>
          HarborlineHomesCo.com
        </li>
        <li>
          <svg viewBox="0 0 24 24"><path d="M12 2a7 7 0 0 0-7 7c0 5 7 13 7 13s7-8 7-13a7 7 0 0 0-7-7zm0 9.5A2.5 2.5 0 1 1 12 6.5a2.5 2.5 0 0 1 0 5z"/></svg>
          <span>2918 E 8250 Suite 207-316<br>Willow Bend, UT 84071</span>
        </li>
      </ul>
    </div>
  </section>

</body>
</html>
```